Wedding Decor and Entertianment business card

Company - We run a weddings and events company called Amber Finch, we provide most entertainment and decor services to our customers.

Initial idea is ....
A simple business card with logo on the front, this will be spot varnish. On a matt black background.
The reverse will be simple contact information.

But happy to try things outside of the box and would welcome some crazy ideas.

Target Market(s)

wedding couples - 21 - 40
High end wedding venues.

Industry/Entity Type

Wedding

Contact Information for Business Card

01492 718 263
amberfinchevents.co.uk
rowan@amberfinchevents.co.uk
or
helena@amberfinchevents.co.uk

Requirements
Nice to have
• black matt background with spot varnish logo on the front.

```html
<!DOCTYPE html>
<html lang="en">
<head>
<meta charset="utf-8">
<title>Amber Finch – Business Card</title>
<link rel="stylesheet" href="https://fonts.googleapis.com/css2?family=Josefin+Sans:wght@300;400;600&display=swap">
<style>
  :root {
    --backdrop: #2b2b2b;
    --card: #0a0a0a;
    --silver: #dcdcdc;
    --silver-soft: #bdbdbd;
    --rule: #5a5a5a;
  }
  * { box-sizing: border-box; margin: 0; padding: 0; }
  html, body {
    width: 1200px; height: 900px; overflow: hidden;
    background: var(--backdrop);
    font-family: "Josefin Sans", sans-serif;
  }
  .stage {
    width: 1200px; height: 900px;
    display: flex; flex-direction: column;
    align-items: center; justify-content: center; gap: 56px;
  }
  .card {
    position: relative;
    width: 640px; height: 366px;
    background: var(--card);
    border-radius: 22px;
    color: var(--silver);
  }
  /* front */
  .brand {
    position: absolute; left: 70px; top: 150px;
    display: flex; align-items: center; gap: 18px;
  }
  .brand-dot {
    width: 38px; height: 38px; border-radius: 50%;
    border: 2px solid var(--silver);
  }
  .brand-name {
    font-weight: 300; font-size: 30px;
    letter-spacing: 0.34em; text-transform: uppercase;
    color: var(--silver);
  }
  .front-email {
    position: absolute; right: 56px; bottom: 44px;
    font-weight: 300; font-size: 18px; letter-spacing: 0.04em;
    color: var(--silver);
  }
  /* back */
  .back-mark {
    position: absolute; left: 70px; top: 88px;
    width: 190px; display: flex; flex-direction: column; align-items: center; gap: 18px;
  }
  .back-mark .brand-dot { width: 120px; height: 120px; border-width: 4px; }
  .back-mark .brand-name { font-size: 17px; letter-spacing: 0.3em; }
  .divider {
    position: absolute; left: 298px; top: 70px;
    width: 1px; height: 220px;
    background: linear-gradient(var(--card), var(--rule) 30%, var(--rule) 70%, var(--card));
  }
  .details { position: absolute; left: 330px; top: 104px; }
  .person {
    font-weight: 600; font-size: 28px; letter-spacing: 0.02em;
    text-transform: uppercase; margin-bottom: 20px;
  }
  .contact-list { list-style: none; }
  .contact-list li {
    display: flex; align-items: center; gap: 12px;
    font-weight: 300; font-size: 17px; letter-spacing: 0.03em;
    line-height: 30px; color: var(--silver-soft);
  }
  .contact-list svg { width: 13px; height: 13px; flex: none; }
</style>
</head>
<body>
<main class="stage">
  <section class="card card-front">
    <div class="brand">
      <span class="brand-dot"></span>
      <span class="brand-name">Amber Finch</span>
    </div>
    <p class="front-email">helena@amberfinchevents.co.uk</p>
  </section>

  <section class="card card-back">
    <div class="back-mark">
      <span class="brand-dot"></span>
      <span class="brand-name">Amber Finch</span>
    </div>
    <span class="divider"></span>
    <div class="details">
      <h1 class="person">Rowan Hale</h1>
      <ul class="contact-list">
        <li>
          <svg viewBox="0 0 16 16" fill="#bdbdbd"><path d="M3.6 1.2l2.2 2.6-1.3 1.6c.9 2 2.3 3.4 4.1 4.2l1.6-1.3 2.6 2.2-1.3 2.6C6.6 13 3 9.4 1.1 3.5z"/></svg>
          01492 718 263
        </li>
        <li>
          <svg viewBox="0 0 16 16" fill="none" stroke="#bdbdbd" stroke-width="1.6"><rect x="1.5" y="3.5" width="13" height="9" rx="1"/><path d="M1.5 4l6.5 5 6.5-5"/></svg>
          rowan@amberfinchevents.co.uk
        </li>
        <li>
          <svg viewBox="0 0 16 16" fill="none" stroke="#bdbdbd" stroke-width="1.4"><circle cx="8" cy="8" r="6.5"/><ellipse cx="8" cy="8" rx="2.8" ry="6.5"/><path d="M1.5 8h13"/></svg>
          www.amberfinchevents.co.uk
        </li>
      </ul>
    </div>
  </section>
</main>
</body>
</html>
```